TLR Property - Business Cards

Looking for a business card & general letterhead, signage etc design for our new logo.

Colours:
000a20
0056a2
00b5ef
0088ce
68cef2

Fonts:
Poppins
Karla

Please keep look and feel of new brand - example in the zip package I sent.

```html
<!DOCTYPE html>
<html lang="en">
<head>
<meta charset="utf-8">
<title>TLR Property – Business Cards</title>
<link rel="stylesheet" href="https://fonts.googleapis.com/css2?family=Poppins:wght@500;600;700&family=Karla:wght@400;500&display=swap">
<style>
  :root {
    --navy-deep: #000a20;
    --navy-card: #10152a;
    --blue-brand: #0056a2;
    --blue-mid: #0088ce;
    --blue-bright: #00b5ef;
    --blue-light: #68cef2;
    --white: #ffffff;
    --muted: #d9deea;
    --backdrop: #2a2b30;
  }
  * { margin: 0; padding: 0; box-sizing: border-box; }
  html, body { width: 1200px; height: 900px; overflow: hidden; }
  body {
    background: var(--backdrop);
    position: relative;
    font-family: "Karla", sans-serif;
  }
  .card {
    position: absolute;
    width: 560px;
    height: 320px;
    border-radius: 22px;
    overflow: hidden;
    box-shadow: 0 18px 40px rgba(0,0,0,.45);
  }

  /* Back of card */
  .card-back {
    left: 60px; top: 100px;
    background: var(--blue-brand);
  }
  .card-back .pattern-area {
    position: absolute; inset: 0;
    background:
      radial-gradient(ellipse 60% 70% at 10% 95%, rgba(104,206,242,.85) 0%, rgba(104,206,242,0) 70%),
      radial-gradient(ellipse 55% 60% at 85% 10%, rgba(10,55,130,.75) 0%, rgba(10,55,130,0) 70%),
      linear-gradient(35deg, var(--blue-mid) 0%, #0a6fc0 35%, var(--blue-brand) 65%, #0b4a94 100%);
  }
  .card-back .brand-lockup {
    position: absolute;
    right: 58px; top: 104px;
    display: flex; align-items: center; gap: 10px;
  }
  .card-back .brand-dot {
    width: 22px; height: 22px;
    border-radius: 50%;
    background: var(--blue-light);
  }
  .card-back .brand-name {
    font-family: "Poppins", sans-serif;
    font-weight: 600;
    font-size: 28px;
    line-height: 1;
    color: var(--white);
    letter-spacing: .3px;
  }

  /* Front of card */
  .card-front {
    left: 580px; top: 470px;
    background: var(--navy-card);
  }
  .card-front .accent-band {
    position: absolute; left: 0; right: 0; bottom: 0;
    height: 12px;
    background: var(--blue-brand);
  }
  .card-front .decor-area {
    position: absolute;
    right: 0; top: 0;
    width: 260px; height: 270px;
    background: radial-gradient(ellipse 60% 60% at 65% 35%, rgba(58,74,154,.55) 0%, rgba(27,35,80,.35) 45%, rgba(16,21,42,0) 80%);
  }
  .card-front .content {
    position: absolute; left: 36px; top: 32px;
  }
  .brand-mark {
    font-family: "Poppins", sans-serif;
    font-weight: 700;
    font-size: 38px;
    line-height: 1;
    color: var(--blue-brand);
    letter-spacing: .3px;
  }
  .person-name {
    margin-top: 24px;
    font-family: "Poppins", sans-serif;
    font-weight: 600;
    font-size: 22px;
    line-height: 1.2;
    color: var(--white);
  }
  .person-role {
    font-family: "Poppins", sans-serif;
    font-weight: 500;
    font-size: 13px;
    color: var(--muted);
    margin-top: 2px;
  }
  .address {
    margin-top: 14px;
    font-size: 13px;
    line-height: 1.35;
    color: var(--muted);
  }
  .contact-list { list-style: none; margin-top: 12px; }
  .contact-list li {
    display: flex; align-items: center; gap: 10px;
    font-size: 13px; color: var(--white);
    line-height: 1.6;
  }
  .contact-list svg { width: 12px; height: 12px; flex: none; }
</style>
</head>
<body>

  <section class="card card-back" aria-label="Card back">
    <div class="pattern-area" role="img" aria-label="Repeating sail pattern fading from light blue at lower left to deep blue at upper right"></div>
    <div class="brand-lockup">
      <span class="brand-dot" aria-hidden="true"></span>
      <span class="brand-name">TLR Property</span>
    </div>
  </section>

  <section class="card card-front" aria-label="Card front">
    <div class="decor-area" role="img" aria-label="Large faint sail decoration"></div>
    <div class="content">
      <div class="brand-mark">TLR Property</div>
      <div class="person-name">Daniel Brooks</div>
      <div class="person-role">Managing Director</div>
      <div class="address">248 Cedar Ridge Lane<br>Harlow, MS 39200</div>
      <ul class="contact-list">
        <li>
          <svg viewBox="0 0 12 12" aria-hidden="true"><path d="M2 1h2.5l1 3-1.5 1a6 6 0 0 0 3 3l1-1.5 3 1V10a1 1 0 0 1-1 1A9.5 9.5 0 0 1 1 2a1 1 0 0 1 1-1z" fill="var(--blue-mid)"/></svg>
          555.210.4470
        </li>
        <li>
          <svg viewBox="0 0 12 12" aria-hidden="true"><rect x="0.5" y="2" width="11" height="8" rx="1" fill="var(--blue-mid)"/><path d="M1 2.5l5 4 5-4" stroke="var(--navy-card)" stroke-width="1" fill="none"/></svg>
          info@tlrproperty.com
        </li>
        <li>
          <svg viewBox="0 0 12 12" aria-hidden="true"><circle cx="6" cy="6" r="5.2" fill="none" stroke="var(--blue-mid)" stroke-width="1.2"/><path d="M1 6h10M6 1c-2 2.5-2 7.5 0 10M6 1c2 2.5 2 7.5 0 10" stroke="var(--blue-mid)" stroke-width="1" fill="none"/></svg>
          www.tlrproperty.com
        </li>
      </ul>
    </div>
    <div class="accent-band"></div>
  </section>

</body>
</html>
```